Laptop Accessories Packing Design

We are looking for a new package design of a laptop accesories (batteries, charges, hard drives etc.). We want to refresh our brand Vireo CellWorks. At VireoCell, we create high-end laptop accessories that ensure reliability, performance, and longevity for users worldwide. Our mission is to deliver innovative and durable solutions that allow users to work, create, and grow without limits.
General Packaging Concept
Minimalist and elegant look, yet with elements that catch the eye (Vireo products will mainly be offered on auction portals such as Brindle, Kiva, Tollmart, so it would be good if the packaging attracted attention and stood out from the competitors).
Should I put a photo, sketch or product icon on the box? We'll leave that to your imagination.
We ask for a general design of the packaging. After the competition, together with the winner, we will add the rest of the information to the back and sides of the box.
In the attachments there is our Logo (you can use other colors) and sample packaging of competitors
Target Market(s)
E-commerse
Industry/Entity Type
individual end customer
Look and feel
Each slider illustrates characteristics of the customer's brand and the style your logo design should communicate.

```html
<!DOCTYPE html>
<html lang="en">
<head>
<meta charset="utf-8">
<title>Vireo CellWorks – Box Design</title>
<link href="https://fonts.googleapis.com/css2?family=Montserrat:wght@500;700;800&display=swap" rel="stylesheet">
<style>
  :root {
    --bg: #f3f3f1;
    --lid: #3a3a38;
    --lid-dark: #2b2b2a;
    --side: #2a2a29;
    --side-dark: #1f1f1e;
    --yellow: #e2bd2c;
    --yellow-soft: #f0c62f;
    --ink: #1c1c1b;
    --white: #ffffff;
    --muted: #d9d9d6;
    --icon: #bdbdba;
  }
  * { box-sizing: border-box; margin: 0; padding: 0; }
  html, body { width: 1200px; height: 654px; overflow: hidden; }
  body {
    background: var(--bg);
    font-family: "Montserrat", Arial, sans-serif;
    position: relative;
  }
  .box-net {
    position: absolute;
    left: 150px; top: 52px;
    width: 900px;
    display: grid;
    grid-template-columns: 150px 750px;
    grid-template-rows: 380px 160px;
  }
  .lid {
    grid-column: 2; grid-row: 1;
    position: relative;
    background: linear-gradient(160deg, var(--lid) 0%, var(--lid-dark) 100%);
    overflow: hidden;
  }
  .side-panel {
    grid-column: 1; grid-row: 2;
    background: linear-gradient(180deg, var(--side) 0%, var(--side-dark) 100%);
  }
  .front {
    grid-column: 2; grid-row: 2;
    position: relative;
    background: linear-gradient(90deg, var(--yellow) 0%, var(--yellow-soft) 100%);
    overflow: hidden;
  }
  .brand-name {
    position: absolute;
    font-weight: 800;
    letter-spacing: -0.5px;
    white-space: nowrap;
  }
  .lid .brand-name { left: 40px; top: 148px; font-size: 34px; color: var(--white); }
  .front .brand-name { right: 90px; top: 50px; font-size: 50px; color: var(--ink); }
  .product-visual {
    position: absolute;
    left: 170px; top: 215px;
    width: 290px; height: 44px;
    border-radius: 10px 10px 6px 6px;
    background: linear-gradient(180deg, #2e2e2d 0%, #1d1d1c 100%);
    box-shadow: 0 10px 18px rgba(0,0,0,0.35);
  }
  .headline {
    position: absolute;
    left: 420px; top: 46px;
    color: var(--yellow-soft);
    font-weight: 800;
    font-size: 16px;
    line-height: 1.15;
    text-align: right;
    width: 190px;
    text-transform: uppercase;
  }
  .disposal-icon { position: absolute; left: 630px; top: 46px; width: 52px; height: 48px; }
  .spec-badge {
    position: absolute;
    left: 612px; top: 116px;
    width: 94px; height: 60px;
    background: var(--yellow-soft);
    border-radius: 12px;
    display: flex; flex-direction: column; align-items: center; justify-content: center;
    gap: 4px;
  }
  .spec-badge .label { font-size: 8px; font-weight: 700; color: var(--ink); }
  .body-copy {
    position: absolute;
    left: 490px; top: 200px;
    width: 220px;
    color: var(--muted);
    font-size: 7px;
    line-height: 1.45;
    font-weight: 500;
  }
</style>
</head>
<body>
  <main class="box-net">
    <section class="lid">
      <div class="brand-name">Vireo CellWorks</div>
      <div class="product-visual" role="img" aria-label="Product photo of a slim black laptop battery"></div>
      <h2 class="headline">Lorem ipsum dolor sit ametelit sed</h2>
      <svg class="disposal-icon" viewBox="0 0 52 48" fill="none" stroke="var(--icon)" stroke-width="2">
        <rect x="14" y="12" width="22" height="28" rx="2"/>
        <line x1="11" y1="10" x2="39" y2="10"/>
        <line x1="21" y1="6" x2="29" y2="6"/>
        <line x1="6" y1="4" x2="46" y2="44"/>
        <line x1="46" y1="4" x2="6" y2="44"/>
      </svg>
      <div class="spec-badge">
        <span class="label">LOREM IP</span>
        <svg width="40" height="18" viewBox="0 0 40 18" fill="none" stroke="#1c1c1b" stroke-width="2">
          <rect x="1" y="2" width="33" height="14" rx="2"/>
          <rect x="35" y="6" width="3" height="6" fill="#1c1c1b"/>
          <line x1="8" y1="5" x2="8" y2="13"/>
          <line x1="14" y1="5" x2="14" y2="13"/>
          <line x1="20" y1="5" x2="20" y2="13"/>
        </svg>
      </div>
      <p class="body-copy">Lorem ipsum dolor sit amet, consectetur adipiscing elit, sed do eiusmod tempor incididunt ut labore et dolore magna aliqua. Quis ipsum suspendisse ultrices gravida. Risus commodo viverra maecenas accumsan lacus vel facilisis.</p>
    </section>
    <section class="side-panel" aria-label="Box end panel"></section>
    <section class="front">
      <div class="brand-name">Vireo CellWorks</div>
    </section>
  </main>
</body>
</html>
```